Hearthkey Homes company website creation

A slick professional landing page it needs to be a very engaging custom designed landing page.

It must have a lead generation tool/box similar to my competitors that will recognise the address when they start to enter the address or postcode.

My main competitors websites to use ideas from to build trust and look correct are: www.brindlecrestholdings.com quillmarshkeys.com

Target Market(s)

People looking to sell their house or property fast. We will buy their property

Industry/Entity Type

Real Estate

Coding

Coded - Design and coding required

Number of Pages Required

1 page

Requirements
Must have
• A lead generation tool that is similar to my competitors to gather their essential details. (please check www.quillmarshkeys.com or www.brindlecrestholdings.com to see what i want.

It also must have all the aspects my competitors has on their landing page. All companies in this industry have this on the landing page. These include: Logos to build trust. Ours can be The Harbinger Logo, the seen on TV logo, The Evening Quorum online logo. Also we need a step by step process map to show the customer how it works.

If the customer is about to leave the page it Must have flash ups that ask the customer to fill in 4 boxes. first name, surname, email, Phone number and address. Check out quillmarshkeys.com to see what i want.

must have a comparison table similar to my competitors. I can include this on the draft.

Must have my frequently asked questions for google SEO ( I will upload these to here to the winner to add this page at the end.

It must be a slick professional design that tells people they are dealing with a company they can trust who has the funds on hand to purchase hundreds of property.
Nice to have
• It must be a slick professional design that tells people they are dealing with a company they can trust who has the funds on hand to purchase hundreds of property.
Should not have
• Anything cheap or tacky looking.

```html
<!DOCTYPE html>
<html lang="en">
<head>
<meta charset="utf-8">
<title>Hearthkey Homes – Landing Page</title>
<link rel="stylesheet" href="https://fonts.googleapis.com/css2?family=Ubuntu:wght@400;500&family=Open+Sans:ital,wght@0,400;0,600;1,400&display=swap">
<style>
:root{
  --board:#8b8b8b;
  --lime:#d5e02d;
  --navy:#2e3956;
  --ink:#1f2329;
  --muted:#8a8a8a;
  --cell:#e1e1e1;
  --band:#f2f2f2;
  --band-warm:#f6f5f3;
  --tick:#3f8a3a;
  --cross:#c9312b;
  --star:#e3a21b;
  --veil:rgba(55,75,130,.78);
}
*{box-sizing:border-box;margin:0;padding:0}
html,body{width:1200px;height:2235px;overflow:hidden}
body{background:var(--board);font-family:"Open Sans",Arial,sans-serif;color:var(--ink);position:relative}
.page{position:absolute;top:53px;width:646px;height:2454px;background:#fff;transform:scale(.8677);transform-origin:0 0;overflow:hidden}
.page--main{left:30px}
.page--popup{left:610px}
.abs{position:absolute}
.heading{font-family:"Ubuntu",sans-serif;font-weight:500;text-transform:uppercase;color:var(--ink);text-align:center;position:absolute;left:0;right:0}
.btn{background:var(--lime);color:var(--ink);font-family:"Ubuntu",sans-serif;font-weight:500;font-size:8px;text-transform:uppercase;display:flex;align-items:center;justify-content:center}
.field{background:#fff;font-size:8px;color:#444;display:flex;align-items:center;padding-left:8px;gap:3px}

/* header */
.site-header{left:0;top:0;width:646px;height:76px;background:#fff}
.phone{left:60px;top:28px;display:flex;align-items:center;gap:4px;font-size:7px;color:#555}
.phone b{font-weight:400;font-size:11px;color:#333}
.brand{left:220px;width:214px;top:28px;display:flex;align-items:center;justify-content:center;gap:7px;font-family:"Ubuntu",sans-serif;font-weight:500;font-size:15px;color:var(--ink)}
.brand i{width:12px;height:12px;background:var(--navy)}
.header-cta{left:489px;top:21px;width:97px;height:27px}
.main-nav{left:0;top:76px;width:646px;height:30px;background:var(--navy);display:flex;justify-content:center;align-items:center;font-size:7px;color:#fff;text-transform:uppercase}
.main-nav span{padding:0 7px;border-left:1px solid rgba(255,255,255,.7);line-height:8px}
.main-nav span:first-child{border:0;color:var(--lime)}

/* hero */
.hero{left:0;top:106px;width:646px;height:345px;background:linear-gradient(180deg,#5d7ea2 0%,#8ea1b3 35%,#c9b89d 55%,#59683f 72%,#3f5a22 100%)}
.hero-title{left:60px;top:212px;font-family:"Ubuntu",sans-serif;font-weight:500;font-size:26px;color:#fff;text-transform:uppercase}
.hero-sub{left:61px;top:251px;font-family:"Ubuntu",sans-serif;font-size:12px;color:#fff}
.hero-points{left:61px;top:280px;display:flex;gap:12px;font-size:8px;color:#fff}
.hero-points i{color:var(--lime);font-style:normal;margin-right:3px}
.hero-input{left:60px;top:309px;width:166px;height:29px}
.hero-btn{left:225px;top:309px;width:102px;height:29px}
.dots{left:303px;top:432px;display:flex;gap:7px}
.dots i{width:5px;height:5px;border-radius:50%;background:#fff}
.dots i:first-child{background:rgba(255,255,255,.45)}

/* process */
.step{position:absolute;top:547px;width:150px;text-align:center}
.step-circle{width:90px;height:90px;margin:0 auto;border-radius:50%;background:var(--lime);border:1px solid #9aa51a;display:flex;align-items:center;justify-content:center}
.step h3{font-family:"Ubuntu",sans-serif;font-weight:500;font-size:7.5px;margin-top:18px;text-transform:uppercase}
.step p{font-size:6.5px;color:var(--muted);line-height:14px;margin-top:5px}
.offer-label{top:740px;font-size:7.5px}
.offer-input{left:190px;top:762px;width:165px;height:29px;background:#f1f1f1}
.offer-btn{left:354px;top:762px;width:102px;height:29px}

/* featured */
.featured{left:0;top:846px;width:646px;height:120px;background:var(--band)}
.press{position:absolute;top:917px;display:flex;align-items:center}
.press--harbinger{left:168px;font-family:"Ubuntu",sans-serif;font-weight:500;font-size:17px;color:#111}
.press--badge{left:317px;top:916px;width:41px;height:30px;border-radius:5px;background:#d62a20}
.press--quorum{left:392px;width:120px;text-align:center;justify-content:center;font-family:"Ubuntu",sans-serif;font-weight:500;font-size:10px;color:#222;line-height:13px}

/* compare table */
.cell{position:absolute;height:27px;font-size:6.5px;display:flex;align-items:center;justify-content:space-between;padding:0 7px;color:#444;background:var(--cell)}
.cell--head{background:var(--navy);color:#fff;text-transform:uppercase;font-weight:600}
.cell--lime{background:var(--lime);color:#333;text-transform:uppercase;font-weight:600}
.tick{color:var(--tick);font-size:8px}
.cross{color:var(--cross);font-size:8px}
.net{top:1282px;font-family:"Ubuntu",sans-serif;font-weight:500;font-size:7.5px;left:122px}
.price{top:1278px;font-family:"Ubuntu",sans-serif;font-size:13px}
.price--good{left:265px;color:var(--tick)}
.price--bad{left:408px;color:var(--cross)}
.note{top:1302px;width:125px;font-size:5.8px;color:var(--muted);line-height:11px}
.rule{left:60px;top:1368px;width:526px;height:1px;background:#e4e4e4}

/* video */
.video{position:absolute;top:1449px;width:171px;height:138px;display:flex;align-items:center;justify-content:center}
.video--a{left:60px;background:linear-gradient(135deg,#cdb69a,#8a6d52 60%,#5a4a3c)}
.video--b{left:237px;background:linear-gradient(135deg,#4a4f58,#c9b7a3 55%,#6b5444)}
.video--c{left:415px;background:linear-gradient(135deg,#5b6c86,#b5a38d 50%,#e6e2da)}

/* testimonials */
.reviews{left:0;top:1643px;width:646px;height:242px;background:var(--band-warm)}
.avatar{position:absolute;top:1718px;width:86px;height:86px;border-radius:50%;border:3px solid #fff;box-shadow:0 0 0 1px #ddd}
.avatar--left{left:37px;background:radial-gradient(circle at 50% 45%,#d9c3ad,#a99179 55%,#6d6a66)}
.avatar--right{left:522px;background:radial-gradient(circle at 50% 45%,#c9b4a2,#4b4f57 55%,#8f99a6)}
.quote{position:absolute;top:1728px;width:180px;font-size:8px;font-style:italic;color:#666;line-height:16px;text-align:justify}
.quote b{font-family:"Ubuntu",sans-serif;font-style:normal;color:#666}
.reviewer{position:absolute;top:1817px;font-size:7px;text-transform:uppercase;color:#333}
.stars{position:absolute;top:1830px;font-size:8px;color:var(--star);letter-spacing:5px}
.review-divider{left:322px;top:1728px;width:1px;height:123px;background:#aaa}

/* about */
.about-copy{left:58px;top:1973px;width:530px;font-size:8.4px;color:#666;text-align:center;line-height:18.4px;font-family:Arial,sans-serif}
.about-photo{left:0;top:2085px;width:646px;height:174px;background:linear-gradient(180deg,#ffffff 0%,#b6c4b0 25%,#7c8f7a 45%,#9ea3a8 65%,#5d6d4e 100%)}

/* footer */
.site-footer{left:0;top:2258px;width:646px;height:196px;background:var(--navy)}
.foot-col{position:absolute;top:2290px;font-family:Arial,sans-serif;font-size:7.5px;color:#fff;line-height:16px}
.foot-col h4{font-weight:400;font-size:7.5px;text-transform:uppercase;margin-bottom:6px}
.foot-row{display:flex;gap:10px;align-items:flex-start;margin-bottom:7px}
.foot-rule{left:60px;top:2406px;width:526px;height:1px;background:rgba(255,255,255,.35)}
.copyright{left:60px;top:2423px;font-size:7.5px;color:#fff;font-family:Arial,sans-serif}
.socials{left:533px;top:2424px;display:flex;gap:6px}
.socials i{width:8px;height:8px;border-radius:50%;background:#fff}

/* popup */
.veil{left:0;top:0;width:646px;height:2454px;background:var(--veil)}
.modal{left:60px;top:96px;width:526px;height:253px;background:#fff}
.modal-title{left:18px;top:34px;font-family:"Ubuntu",sans-serif;font-weight:500;font-size:15px;letter-spacing:.3px}
.modal-field{position:absolute;height:26px;border:1px solid #c9c9c9;font-size:7.5px;color:#444;padding:7px 6px}
.modal-submit{left:15px;top:189px;width:254px;height:28px}
.modal-photo{left:293px;top:0;width:233px;height:253px;background:linear-gradient(180deg,#6e96c6 0%,#b7c9dc 30%,#d8d2c4 50%,#7a6a54 70%,#3f6f96 88%,#2b4c6b 100%)}
.modal-close{left:498px;top:8px;width:19px;height:17px;border:1px solid #fff;color:#fff;font-size:9px;display:flex;align-items:center;justify-content:center}
</style>
</head>
<body>

<main class="page page--main">
  <header class="abs site-header">
    <div class="abs phone">
      <svg width="8" height="13" viewBox="0 0 8 13"><rect x=".6" y=".6" width="6.8" height="11.8" rx="1.2" fill="none" stroke="#555" stroke-width="1.2"/><rect x="3" y="10" width="2" height="1" fill="#555"/></svg>
      PHONE - <b>888-888-8888</b>
    </div>
    <div class="abs brand"><i></i>Hearthkey Homes</div>
    <div class="abs btn header-cta">Get a cash offer</div>
  </header>
  <nav class="abs main-nav">
    <span>Home</span><span>How it works</span><span>Sell house fast</span><span>Cash house buyers</span><span>Value my house</span><span>More services</span><span>About us</span>
  </nav>

  <section class="abs hero" role="img" aria-label="Photo of a modern gabled house lit up at dusk on a lawn"></section>
  <h1 class="abs hero-title">Hearthkey Homes</h1>
  <p class="abs hero-sub">We will buy any type of property fast</p>
  <div class="abs hero-points"><span><i>★</i>Lorem Ipsum</span><span><i>★</i>Lorem Ipsum</span><span><i>★</i>Lorem Ipsum</span></div>
  <div class="abs field hero-input">
    <svg width="6" height="8" viewBox="0 0 6 8"><path d="M3 0a3 3 0 0 1 3 3c0 2-3 5-3 5S0 5 0 3a3 3 0 0 1 3-3z" fill="#333"/><circle cx="3" cy="3" r="1" fill="#fff"/></svg>Address or Postcode
  </div>
  <div class="abs btn hero-btn">Request valuation</div>
  <div class="abs dots"><i></i><i></i><i></i><i></i></div>

  <h2 class="heading" style="top:503px;font-size:20px">The process is simple</h2>
  <div class="step" style="left:91px">
    <div class="step-circle"><svg width="40" height="40" viewBox="0 0 40 40" fill="none" stroke="#222" stroke-width="1.6"><rect x="7" y="5" width="22" height="30"/><path d="M11 12h14M11 17h14M11 22h10M11 27h8"/><path d="M33 10l-9 16-2 4 4-3 9-16z"/></svg></div>
    <h3>Fill in online form</h3>
    <p>Nemo enim ipsam voluptatem quia voluptas sit aspernatur aut odit autconsequuntur magni dolores eos qui ratione</p>
  </div>
  <div class="step" style="left:248px">
    <div class="step-circle"><svg width="40" height="40" viewBox="0 0 40 40" fill="none" stroke="#222" stroke-width="1.6"><path d="M5 17v18h30V17"/><path d="M5 17l15 11 15-11"/><rect x="10" y="6" width="20" height="14"/><path d="M14 12h12"/></svg></div>
    <h3>Receive offer</h3>
    <p>Nemo enim ipsam voluptatem quia voluptas sit aspernatur aut odit autconsequuntur magni dolores eos qui ratione</p>
  </div>
  <div class="step" style="left:405px">
    <div class="step-circle"><svg width="40" height="40" viewBox="0 0 40 40" fill="none" stroke="#222" stroke-width="1.6"><path d="M20 6l-11 13M20 6l11 13"/><circle cx="20" cy="6" r="1.5"/><rect x="6" y="19" width="28" height="13" rx="2"/></svg></div>
    <h3>Sale agreed</h3>
    <p>Nemo enim ipsam voluptatem quia voluptas sit aspernatur aut odit autconsequuntur magni dolores eos qui ratione</p>
  </div>
  <p class="heading offer-label">Start with a free cash offer</p>
  <div class="abs field offer-input">
    <svg width="6" height="8" viewBox="0 0 6 8"><path d="M3 0a3 3 0 0 1 3 3c0 2-3 5-3 5S0 5 0 3a3 3 0 0 1 3-3z" fill="#333"/><circle cx="3" cy="3" r="1" fill="#fff"/></svg>Address or Postcode
  </div>
  <div class="abs btn offer-btn">Get a cash offer</div>

  <section class="abs featured"></section>
  <h2 class="heading" style="top:865px;font-size:20px">As featured on</h2>
  <div class="press press--harbinger">The Harbinger</div>
  <div class="press press--badge" role="img" aria-label="As seen on TV badge"></div>
  <div class="press press--quorum">The Evening Quorum<br>online</div>

  <h2 class="heading" style="top:1020px;font-size:16px">Why sell your property to Brindlecrest Holdings</h2>
  <div class="cell cell--head" style="left:115px;top:1055px;width:129px">Checklist</div>
  <div class="cell cell--head" style="left:258px;top:1055px;width:129px">Selling to Brindlecrest</div>
  <div class="cell cell--head" style="left:401px;top:1055px;width:129px">Selling via estate agents</div>
  <div class="cell cell--lime" style="left:115px;top:1087px;width:129px">Potential timetable</div>
  <div class="cell cell--lime" style="left:258px;top:1087px;width:129px">Within days</div>
  <div class="cell cell--lime" style="left:401px;top:1087px;width:129px;font-size:5.8px">It could be 6 months, or longer</div>
  <div class="cell" style="left:115px;top:1118px;width:129px">Lorem ipsum dolor</div>
  <div class="cell" style="left:258px;top:1118px;width:129px">€ 100.000</div>
  <div class="cell" style="left:401px;top:1118px;width:129px">€ 100.000</div>
  <div class="cell" style="left:115px;top:1149px;width:129px">Lorem ipsum dolor</div>
  <div class="cell" style="left:258px;top:1149px;width:129px">€ 100.000</div>
  <div class="cell" style="left:401px;top:1149px;width:129px">€ 100.000</div>
  <div class="cell" style="left:115px;top:1180px;width:129px">Lorem ipsum dolor</div>
  <div class="cell" style="left:258px;top:1180px;width:129px">€ 100.000<span class="tick">✓</span></div>
  <div class="cell" style="left:401px;top:1180px;width:129px">€ 100.000<span class="cross">✕</span></div>
  <div class="cell" style="left:115px;top:1211px;width:129px">Lorem ipsum dolor</div>
  <div class="cell" style="left:258px;top:1211px;width:129px">€ 100.000<span class="tick">✓</span></div>
  <div class="cell" style="left:401px;top:1211px;width:129px">€ 100.000<span class="cross">✕</span></div>
  <div class="cell" style="left:115px;top:1242px;width:129px">Lorem ipsum dolor</div>
  <div class="cell" style="left:258px;top:1242px;width:129px">€ 100.000<span class="tick">✓</span></div>
  <div class="cell" style="left:401px;top:1242px;width:129px">€ 100.000<span class="cross">✕</span></div>

  <div class="abs net">NET PRICE ACHIEVED</div>
  <div class="abs price price--good">€ 80.000</div>
  <div class="abs price price--bad">€ 80.000</div>
  <p class="abs note" style="left:266px">Nemo enim ipsam voluptatem voluptas sit aspernatur aut odit aut fugit,</p>
  <p class="abs note" style="left:409px">Nemo enim ipsam voluptatem voluptas sit aspernatur aut odit aut fugit,</p>
  <div class="abs rule"></div>

  <h2 class="heading" style="top:1414px;font-size:14.5px">See how the process works when selling your home</h2>
  <div class="video video--a" role="img" aria-label="Video still: hands signing papers beside a small model house"><svg width="20" height="20" viewBox="0 0 20 20"><circle cx="10" cy="10" r="8.5" fill="none" stroke="#fff" stroke-width="2"/><path d="M8 6l6 4-6 4z" fill="#fff"/></svg></div>
  <div class="video video--b" role="img" aria-label="Video still: house keys handed over"><svg width="20" height="20" viewBox="0 0 20 20"><circle cx="10" cy="10" r="8.5" fill="none" stroke="#fff" stroke-width="2"/><path d="M8 6l6 4-6 4z" fill="#fff"/></svg></div>
  <div class="video video--c" role="img" aria-label="Video still: handshake over a contract on a desk"><svg width="20" height="20" viewBox="0 0 20 20"><circle cx="10" cy="10" r="8.5" fill="none" stroke="#fff" stroke-width="2"/><path d="M8 6l6 4-6 4z" fill="#fff"/></svg></div>

  <section class="abs reviews"></section>
  <h2 class="heading" style="top:1671px;font-size:20px">What customer are saying</h2>
  <div class="avatar avatar--left" role="img" aria-label="Portrait photo of a smiling customer"></div>
  <p class="quote" style="left:128px"><b>❝</b>Nemo enim ipsam voluptatem quia voluptas sit aspernatur aut odit aut fugit, sed quia consequuntur magni dolores eos qui ratione voluptatem sequi nesciuntNemo enim ipsam voluptatem quia voluptas <b>❞</b></p>
  <div class="reviewer" style="left:139px">Carver, Newyork</div>
  <div class="stars" style="left:139px">★★★★★</div>
  <div class="abs review-divider"></div>
  <p class="quote" style="left:336px"><b>❝</b>Nemo enim ipsam voluptatem quia voluptas sit aspernatur aut odit aut fugit, sed quia consequuntur magni dolores eos qui ratione voluptatem sequi nesciuntNemo enim ipsam voluptatem quia voluptas <b>❞</b></p>
  <div class="reviewer" style="left:347px">Dorian Pell, Newyork</div>
  <div class="stars" style="left:347px">★★★★★</div>
  <div class="avatar avatar--right" role="img" aria-label="Portrait photo of a customer in a suit on the phone"></div>

  <h2 class="heading" style="top:1937px;font-size:20px">About Hearthkey Homes</h2>
  <p class="abs about-copy">Sed ut perspiciatis unde omnis iste natus error sit voluptatem accusantium doloremque laudantium, totam rem aperiam, eaque ipsa quae ab illo inventore veritatis et quasi architecto beatae vitae dicta sunt explicabo. Nemo enim ipsam voluptatem quia voluptas sit aspernatur aut odit aut fugit, sed quia consequuntur magni dolores eos qui ratione voluptatem sequi nesciunt. Neque porro quisquam est, qui dolorem ipsum quia dolor sit amet, consectetur, adipisci velit, sed quia non numquam eius modi tempora incidunt ut labore et dolore magnam aliquam quaerat voluptatem. Ut enim ad minima veniam, quis nostrum exercitationem ullam corporis suscipit laboriosam, nisi ut aliquid ex ea commodi consequatu</p>
  <div class="abs about-photo" role="img" aria-label="Photo of a single-storey suburban house with a garage and trees"></div>

  <footer class="abs site-footer"></footer>
  <div class="foot-col" style="left:60px;width:150px"><h4>About us</h4>Sed ut perspiciatis unde omnis iste natus error sit&nbsp; doloremque laudantium, aperiam, eaque ipsa quae ab</div>
  <div class="foot-col" style="left:240px"><h4>Services</h4>Lorem ipsum dolor<br>Lorem ipsum dolor<br>Lorem ipsum dolor</div>
  <div class="foot-col" style="left:357px"><h4>Information hub</h4>Case studies<br>News<br>Guides<br>Videos<br>Cities</div>
  <div class="foot-col" style="left:463px;width:135px"><h4>Contact us</h4>
    <div class="foot-row"><svg width="9" height="9" viewBox="0 0 9 9"><path d="M1 1h2l1 2-1 1c.6 1.2 1.4 2 2.6 2.6l1-1 2 1v2c-4 .4-8-3.6-7.6-7.6z" fill="none" stroke="#fff" stroke-width=".8"/></svg>888-888-8888</div>
    <div class="foot-row"><svg width="7" height="9" viewBox="0 0 6 8"><path d="M3 0a3 3 0 0 1 3 3c0 2-3 5-3 5S0 5 0 3a3 3 0 0 1 3-3z" fill="#fff"/><circle cx="3" cy="3" r="1" fill="#2e3956"/></svg><span>Lorem ipsum dolor sit amet, consectetur adipiscing elit</span></div>
    <div class="foot-row"><svg width="9" height="7" viewBox="0 0 9 7"><rect x=".4" y=".4" width="8.2" height="6.2" fill="none" stroke="#fff" stroke-width=".8"/><path d="M.5.5l4 3 4-3" fill="none" stroke="#fff" stroke-width=".8"/></svg>hearthkeyhomes.co.uk</div>
  </div>
  <div class="abs foot-rule"></div>
  <div class="abs copyright">© 2020 All Rights Reserved</div>
  <div class="abs socials"><i></i><i></i><i></i><i></i></div>
</main>

<main class="page page--popup">
  <header class="abs site-header">
    <div class="abs phone">
      <svg width="8" height="13" viewBox="0 0 8 13"><rect x=".6" y=".6" width="6.8" height="11.8" rx="1.2" fill="none" stroke="#555" stroke-width="1.2"/><rect x="3" y="10" width="2" height="1" fill="#555"/></svg>
      PHONE - <b>888-888-8888</b>
    </div>
    <div class="abs brand"><i></i>Hearthkey Homes</div>
    <div class="abs btn header-cta">Get a cash offer</div>
  </header>
  <nav class="abs main-nav">
    <span>Home</span><span>How it works</span><span>Sell house fast</span><span>Cash house buyers</span><span>Value my house</span><span>More services</span><span>About us</span>
  </nav>
  <section class="abs hero" role="img" aria-label="Photo of a modern gabled house lit up at dusk on a lawn"></section>
  <div class="abs dots"><i></i><i></i><i></i><i></i></div>

  <h2 class="heading" style="top:503px;font-size:20px">The process is simple</h2>
  <div class="step" style="left:91px"><div class="step-circle"></div><h3>Fill in online form</h3><p>Nemo enim ipsam voluptatem quia voluptas sit aspernatur aut odit autconsequuntur magni dolores eos qui ratione</p></div>
  <div class="step" style="left:248px"><div class="step-circle"></div><h3>Receive offer</h3><p>Nemo enim ipsam voluptatem quia voluptas sit aspernatur aut odit autconsequuntur magni dolores eos qui ratione</p></div>
  <div class="step" style="left:405px"><div class="step-circle"></div><h3>Sale agreed</h3><p>Nemo enim ipsam voluptatem quia voluptas sit aspernatur aut odit autconsequuntur magni dolores eos qui ratione</p></div>
  <p class="heading offer-label">Start with a free cash offer</p>
  <div class="abs field offer-input">Address or Postcode</div>
  <div class="abs btn offer-btn">Get a cash offer</div>

  <section class="abs featured"></section>
  <h2 class="heading" style="top:865px;font-size:20px">As featured on</h2>
  <div class="press press--harbinger">The Harbinger</div>
  <div class="press press--badge" role="img" aria-label="As seen on TV badge"></div>
  <div class="press press--quorum">The Evening Quorum<br>online</div>

  <h2 class="heading" style="top:1020px;font-size:16px">Why sell your property to Brindlecrest Holdings</h2>
  <div class="cell cell--head" style="left:115px;top:1055px;width:129px">Checklist</div>
  <div class="cell cell--head" style="left:258px;top:1055px;width:129px">Selling to Brindlecrest</div>
  <div class="cell cell--head" style="left:401px;top:1055px;width:129px">Selling via estate agents</div>
  <div class="cell cell--lime" style="left:115px;top:1087px;width:129px">Potential timetable</div>
  <div class="cell cell--lime" style="left:258px;top:1087px;width:129px">Within days</div>
  <div class="cell cell--lime" style="left:401px;top:1087px;width:129px;font-size:5.8px">It could be 6 months, or longer</div>
  <div class="cell" style="left:115px;top:1118px;width:129px">Lorem ipsum dolor</div>
  <div class="cell" style="left:258px;top:1118px;width:129px">€ 100.000</div>
  <div class="cell" style="left:401px;top:1118px;width:129px">€ 100.000</div>
  <div class="cell" style="left:115px;top:1149px;width:129px">Lorem ipsum dolor</div>
  <div class="cell" style="left:258px;top:1149px;width:129px">€ 100.000</div>
  <div class="cell" style="left:401px;top:1149px;width:129px">€ 100.000</div>
  <div class="cell" style="left:115px;top:1180px;width:129px">Lorem ipsum dolor</div>
  <div class="cell" style="left:258px;top:1180px;width:129px">€ 100.000<span class="tick">✓</span></div>
  <div class="cell" style="left:401px;top:1180px;width:129px">€ 100.000<span class="cross">✕</span></div>
  <div class="cell" style="left:115px;top:1211px;width:129px">Lorem ipsum dolor</div>
  <div class="cell" style="left:258px;top:1211px;width:129px">€ 100.000<span class="tick">✓</span></div>
  <div class="cell" style="left:401px;top:1211px;width:129px">€ 100.000<span class="cross">✕</span></div>
  <div class="cell" style="left:115px;top:1242px;width:129px">Lorem ipsum dolor</div>
  <div class="cell" style="left:258px;top:1242px;width:129px">€ 100.000<span class="tick">✓</span></div>
  <div class="cell" style="left:401px;top:1242px;width:129px">€ 100.000<span class="cross">✕</span></div>
  <div class="abs net">NET PRICE ACHIEVED</div>
  <div class="abs price price--good">€ 80.000</div>
  <div class="abs price price--bad">€ 80.000</div>
  <p class="abs note" style="left:266px">Nemo enim ipsam voluptatem voluptas sit aspernatur aut odit aut fugit,</p>
  <p class="abs note" style="left:409px">Nemo enim ipsam voluptatem voluptas sit aspernatur aut odit aut fugit,</p>

  <h2 class="heading" style="top:1414px;font-size:14.5px">See how the process works when selling your home</h2>
  <div class="video video--a" role="img" aria-label="Video still: hands signing papers beside a small model house"></div>
  <div class="video video--b" role="img" aria-label="Video still: house keys handed over"></div>
  <div class="video video--c" role="img" aria-label="Video still: handshake over a contract on a desk"></div>

  <section class="abs reviews"></section>
  <h2 class="heading" style="top:1671px;font-size:20px">What customer are saying</h2>
  <div class="avatar avatar--left" role="img" aria-label="Portrait photo of a smiling customer"></div>
  <p class="quote" style="left:128px">Nemo enim ipsam voluptatem quia voluptas sit aspernatur aut odit aut fugit, sed quia consequuntur magni dolores eos qui ratione voluptatem sequi nesciuntNemo enim ipsam voluptatem quia voluptas</p>
  <div class="reviewer" style="left:139px">Carver, Newyork</div>
  <div class="stars" style="left:139px">★★★★★</div>
  <div class="abs review-divider"></div>
  <p class="quote" style="left:336px">Nemo enim ipsam voluptatem quia voluptas sit aspernatur aut odit aut fugit, sed quia consequuntur magni dolores eos qui ratione voluptatem sequi nesciuntNemo enim ipsam voluptatem quia voluptas</p>
  <div class="reviewer" style="left:347px">Dorian Pell, Newyork</div>
  <div class="stars" style="left:347px">★★★★★</div>
  <div class="avatar avatar--right" role="img" aria-label="Portrait photo of a customer in a suit on the phone"></div>

  <h2 class="heading" style="top:1937px;font-size:20px">About Hearthkey Homes</h2>
  <p class="abs about-copy">Sed ut perspiciatis unde omnis iste natus error sit voluptatem accusantium doloremque laudantium, totam rem aperiam, eaque ipsa quae ab illo inventore veritatis et quasi architecto beatae vitae dicta sunt explicabo. Nemo enim ipsam voluptatem quia voluptas sit aspernatur aut odit aut fugit, sed quia consequuntur magni dolores eos qui ratione voluptatem sequi nesciunt. Neque porro quisquam est, qui dolorem ipsum quia dolor sit amet, consectetur, adipisci velit, sed quia non numquam eius modi tempora incidunt ut labore et dolore magnam aliquam quaerat voluptatem. Ut enim ad minima veniam, quis nostrum exercitationem ullam corporis suscipit laboriosam, nisi ut aliquid ex ea commodi consequatu</p>
  <div class="abs about-photo" role="img" aria-label="Photo of a single-storey suburban house with a garage and trees"></div>

  <footer class="abs site-footer"></footer>
  <div class="foot-col" style="left:60px;width:150px"><h4>About us</h4>Sed ut perspiciatis unde omnis iste natus error sit&nbsp; doloremque laudantium, aperiam, eaque ipsa quae ab</div>
  <div class="foot-col" style="left:240px"><h4>Services</h4>Lorem ipsum dolor<br>Lorem ipsum dolor<br>Lorem ipsum dolor</div>
  <div class="foot-col" style="left:357px"><h4>Information hub</h4>Case studies<br>News<br>Guides<br>Videos<br>Cities</div>
  <div class="foot-col" style="left:463px;width:135px"><h4>Contact us</h4>
    <div class="foot-row">888-888-8888</div>
    <div class="foot-row">Lorem ipsum dolor sit amet, consectetur adipiscing elit</div>
    <div class="foot-row">hearthkeyhomes.co.uk</div>
  </div>
  <div class="abs foot-rule"></div>
  <div class="abs copyright">© 2020 All Rights Reserved</div>
  <div class="abs socials"><i></i><i></i><i></i><i></i></div>

  <div class="abs veil"></div>

  <div class="abs modal" role="dialog" aria-label="Make an appointment">
    <h2 class="abs modal-title">MAKE AN APPOINTMENT</h2>
    <div class="modal-field" style="left:15px;top:78px;width:125px">First Name</div>
    <div class="modal-field" style="left:144px;top:78px;width:125px">Surname</div>
    <div class="modal-field" style="left:15px;top:111px;width:125px">Email</div>
    <div class="modal-field" style="left:144px;top:111px;width:125px">Phone Number</div>
    <div class="modal-field" style="left:15px;top:144px;width:254px;height:41px">Type here</div>
    <div class="abs btn modal-submit">Submit now</div>
    <div class="abs modal-photo" role="img" aria-label="Photo of a modern white villa with wooden shutters beside a lit pool"></div>
    <div class="abs modal-close">X</div>
  </div>
</main>

</body>
</html>
```